tourism marketplace web app redesign*

Hi, I need our front-page redesigned. For the competition please submit a jpg of ABOVE THE FOLD ONLY. The full page redesign will be a revision request. URL is https://qp.vendomix.hu/hu/index.html login:'fullhd' and password:'asdasd' (Fold is supposed to be at "Kiemelt Ajanlatok", use all elements above that. Please use at least one extra color other than the two in the logo, or you may completely change them. FOCUS should be on the central combined search box (3 dropdown, 2 calendar picker + Kereses Button) just like lodgewave.com, staynook.com, Torvil.com, etc... The search box is always large, central, white, we want that too. We want it to look more modern, more clean AND we want to feature a changing beautiful nature photo background (like lodgewave.com).Please use our newly designed logo (in attached pdf) and use that new spelling: "fieldtrek.online"

```html
<!DOCTYPE html>
<html lang="hu">
<head>
<meta charset="utf-8">
<title>fieldtrek.online – Főoldal</title>
<link href="https://fonts.googleapis.com/css2?family=Fira+Sans+Condensed:wght@400;500;600&family=Fira+Sans:wght@400;500&display=swap" rel="stylesheet">
<style>
:root{
  --dark:#1b1b1b;
  --teal:#5fb39a;
  --amber:#f7b033;
  --white:#ffffff;
  --ink:#1e1e1e;
  --muted:#9a9a9a;
  --hero-top:#8a9498;
  --hero-mid:#7c8a6c;
  --hero-low:#6f7a2e;
}
*{box-sizing:border-box;margin:0;padding:0}
html,body{width:1200px;height:895px;overflow:hidden;background:var(--white);font-family:"Fira Sans",sans-serif;color:var(--ink)}
.site-header{height:50px;background:var(--dark);position:relative}
.brand{position:absolute;left:220px;top:6px;display:flex;align-items:center;gap:8px}
.brand-dot{width:38px;height:38px;border-radius:50%;background:var(--teal)}
.brand-name{font-family:"Fira Sans",sans-serif;font-weight:500;font-size:17px;color:var(--white)}
.main-nav{position:absolute;right:220px;top:14px;display:flex;align-items:center;gap:13px;font-family:"Fira Sans Condensed",sans-serif;font-weight:600;font-size:11.5px;color:var(--white);text-transform:uppercase}
.partner-btn{border:1.5px solid var(--teal);border-radius:3px;color:var(--teal);padding:5px 8px;display:flex;align-items:center;gap:5px;margin-left:0;margin-top:-5px}
.hero{position:relative;height:437px;background:linear-gradient(180deg,#9aa0a2 0%,#8a9aa3 22%,#7e8f7a 45%,#879463 62%,#6b7531 85%,#4f5624 100%)}
.hero-photo{position:absolute;inset:0}
.hero-title{position:absolute;top:169px;left:0;right:0;display:flex;justify-content:center;font-family:"Fira Sans Condensed",sans-serif;font-weight:500;font-size:22.5px;line-height:26px;color:var(--white);text-transform:uppercase}
.hero-title .left{text-align:right;padding-right:9px;border-right:2px solid var(--amber)}
.hero-title .right{padding-left:9px}
.search-box{position:absolute;left:282px;top:247px;width:635px;height:43px;background:var(--dark);border-radius:4px;display:flex;gap:3px;padding:3px}
.field{background:var(--white);border-radius:2px;display:flex;align-items:center;justify-content:space-between;padding:0 8px 0 12px;font-size:9px}
.field.w1{width:118px}.field.w2{width:126px}.field.w3{width:126px}
.field.date{width:126px;justify-content:flex-start;gap:20px;padding-left:8px;font-size:8px}
.search-btn{flex:1;background:var(--amber);border-radius:2px;display:flex;align-items:center;justify-content:center;font-family:"Fira Sans Condensed",sans-serif;font-weight:600;font-size:11px;color:var(--ink)}
.featured h2{position:absolute;top:524px;left:0;right:0;text-align:center;font-family:"Fira Sans Condensed",sans-serif;font-weight:500;font-size:20px}
.offer{position:absolute;top:575px;width:240px}
.offer-img{height:160px;position:relative}
.offer-img .name{position:absolute;left:12px;top:13px;font-family:"Fira Sans Condensed",sans-serif;font-weight:600;font-size:12.5px;line-height:15.5px;color:var(--white);text-transform:uppercase}
.offer-meta{display:flex;justify-content:space-between;margin-top:11px;font-size:11.5px}
.offer-meta b{font-weight:500}
.offer p{margin-top:8px;font-size:8px;line-height:10.7px;padding-right:20px}
.arrow{position:absolute;top:642px;width:26px;height:26px}
.pager{position:absolute;top:822px;left:0;right:0;display:flex;justify-content:center;gap:11px;font-family:"Fira Sans Condensed",sans-serif;font-size:11px;color:var(--muted)}
.pager .on{color:var(--teal)}
</style>
</head>
<body>
<header class="site-header">
  <div class="brand"><span class="brand-dot"></span><span class="brand-name">fieldtrek.online</span></div>
  <nav class="main-nav">
    <span>Országok</span><span>Vadfajok</span><span>Rólunk</span><span>ÁSZF</span><span>Hogyan működik</span>
    <span class="partner-btn"><svg width="9" height="9" viewBox="0 0 10 10"><circle cx="5" cy="5" r="5" fill="#5fb39a"/><path d="M5 2.5v5M2.5 5h5" stroke="#1b1b1b" stroke-width="1.4"/></svg>Legyen partnerünk</span>
  </nav>
</header>

<section class="hero">
  <div class="hero-photo" role="img" aria-label="Ködös alpesi rét fenyőkkel, faházakkal és hegyekkel a háttérben"></div>
  <h1 class="hero-title"><span class="left">Nincs szükséged<br>vadászatszervezőre!</span><span class="right">Foglalj közvetlen<br>a vadászterületnél</span></h1>
  <form class="search-box">
    <div class="field w1">Összes vad<svg width="7" height="14" viewBox="0 0 7 14"><path d="M1 5l2.5-3L6 5M1 9l2.5 3L6 9" fill="none" stroke="#999" stroke-width="1"/></svg></div>
    <div class="field w2">Összes ország<svg width="7" height="14" viewBox="0 0 7 14"><path d="M1 5l2.5-3L6 5M1 9l2.5 3L6 9" fill="none" stroke="#999" stroke-width="1"/></svg></div>
    <div class="field w3">Összes ajánlat<svg width="7" height="14" viewBox="0 0 7 14"><path d="M1 5l2.5-3L6 5M1 9l2.5 3L6 9" fill="none" stroke="#999" stroke-width="1"/></svg></div>
    <div class="field date"><svg width="14" height="14" viewBox="0 0 14 14"><rect x="1" y="2" width="12" height="11" fill="none" stroke="#999"/><path d="M1 5h12" stroke="#999"/><path d="M4 1v2M10 1v2" stroke="#999"/></svg>19.08.07 - 19.08.14</div>
    <div class="search-btn">KERESÉS</div>
  </form>
</section>

<section class="featured">
  <h2>KIEMELT AJÁNLATOK</h2>
  <svg class="arrow" style="left:174px" viewBox="0 0 26 26"><circle cx="13" cy="13" r="12" fill="none" stroke="#ccc" stroke-width="1.3"/><path d="M18 13H8M11 10l-3 3 3 3" fill="none" stroke="#bbb" stroke-width="1.2"/></svg>
  <svg class="arrow" style="left:1000px" viewBox="0 0 26 26"><circle cx="13" cy="13" r="12" fill="none" stroke="#5fb39a" stroke-width="1.3"/><path d="M8 13h10M15 10l3 3-3 3" fill="none" stroke="#5fb39a" stroke-width="1.2"/></svg>

  <article class="offer" style="left:220px">
    <div class="offer-img" role="img" aria-label="Barnamedve bocsokkal erdei sziklák között" style="background:linear-gradient(160deg,#4d5a3a,#5d5246 55%,#8a8a82)"><span class="name">Ötödik<br>ajánlat<br>neve</span></div>
    <div class="offer-meta"><span>Város neve, Hungary</span><b>1.234 €-tol</b></div>
    <p>Lorem ipsum dolor sit amet, consectetuer adipiscing elit, sed diam nonummy nibh euismod tincidunt ut laoreet dolore magna aliquam erat volutpat.</p>
  </article>
  <article class="offer" style="left:480px">
    <div class="offer-img" role="img" aria-label="Vörös róka napfényes erdőszélen" style="background:linear-gradient(160deg,#2f3a22,#6b5a32 50%,#b58a4a)"><span class="name">Második<br>ajánlat<br>neve</span></div>
    <div class="offer-meta"><span>Város neve, Hungary</span><b>1.234 €-tol</b></div>
    <p>Lorem ipsum dolor sit amet, consectetuer adipiscing elit, sed diam nonummy nibh euismod tincidunt ut laoreet dolore magna aliquam erat volutpat.</p>
  </article>
  <article class="offer" style="left:740px">
    <div class="offer-img" role="img" aria-label="Gímszarvas bika erdei úton" style="background:linear-gradient(180deg,#3d5a32,#55704a 50%,#a8a49a)"><span class="name">Harmadik<br>ajánlat<br>neve</span></div>
    <div class="offer-meta"><span>Város neve, Hungary</span><b>1.234 €-tol</b></div>
    <p>Lorem ipsum dolor sit amet, consectetuer adipiscing elit, sed diam nonummy nibh euismod tincidunt ut laoreet dolore magna aliquam erat volutpat.</p>
  </article>

  <nav class="pager"><span class="on">1</span><span>2</span><span>3</span><span>4</span><span>5</span><span>TOVÁBBI AJÁNLATOK</span></nav>
</section>
</body>
</html>
```